Professional stationery for boutique management consulting business

I need branded business stationery for my consulting business, using our existing logo and website branding. We consult to senior executives to create deep cultural change needed for humane, people-centred workplaces. The key deliverables are: (A4 size) business letterheads, proposal cover, project folder, report template, email footer, business card, simple powerpoint template. A warm, empowering and expert tone of voice is important as it needs to bridge the gap between academia and industry. It should be clean and professional without feeling "over-branded".
I would like to see stationery designs that use my website colours and design elements (see attached file), especially the delta logo. Our fonts are Operetta and Sofia Pro.
Updates

Thanks for the designs sent so far. Just to confirm that our key deliverables for this project are: - (A4 size) business letterhead - (A4 size) proposal template - (A4 size) report template - Project folder, - Simple powerpoint template - Business card Many thanks

Target Market(s)

Senior executives and business professionals with an interest in business school thinking.

Industry/Entity Type

Management consulting and executive coaching

Font styles to use
Other font styles liked:
• Operetta and Sofia Pro

Colors
0054AA
0677BA
7BADD7
CADEEF
E8F1F8

Requirements
Must have
• Clean professional design that ties in closely to complement and extend the design elements in my website: marlowadvises.com
Nice to have
• Address and contact details I can edit in Microsoft Word, Outlook for Mac, etc
Should not have
• Excessive brand elements, fussy design and additional colours.

```html
<!DOCTYPE html>
<html lang="en">
<head>
<meta charset="utf-8">
<title>Marlow Advises – Stationery Suite</title>
<link rel="stylesheet" href="https://fonts.googleapis.com/css2?family=Playfair+Display:wght@400;700&family=Nunito+Sans:wght@400;700&display=swap">
<style>
  :root{
    --blue:#0054AA;
    --blue-mid:#0677BA;
    --blue-soft:#7BADD7;
    --blue-pale:#CADEEF;
    --blue-mist:#E8F1F8;
    --ink:#2b2f36;
    --paper:#ffffff;
    --slide:#f1f4f7;
    --backdrop:#a9aaae;
    --serif:'Playfair Display', Georgia, serif;
    --sans:'Nunito Sans', Arial, sans-serif;
  }
  *{box-sizing:border-box;margin:0;padding:0}
  html,body{width:1200px;height:857px;overflow:hidden}
  body{background:var(--backdrop);position:relative;font-family:var(--sans);color:var(--ink)}
  .piece{position:absolute;background:var(--paper);overflow:hidden;box-shadow:0 1px 3px rgba(0,0,0,.18)}
  .wordmark{font-family:var(--serif);font-weight:400;color:var(--blue);line-height:.9;display:flex;align-items:center;gap:.35em}
  .wordmark::before{content:"";width:.55em;height:.55em;background:var(--blue);border-radius:50%;flex:none}
  .wordmark span{display:block}
  .contacts{font-size:3.3px;line-height:1.5;color:var(--ink)}
  .contacts li{list-style:none;display:flex;align-items:center;gap:2px}
  .contacts li::before{content:"";width:2.4px;height:2.4px;border-radius:50%;background:var(--blue);flex:none}
  .photo{background:linear-gradient(160deg,#8fa07a,#3b5687 60%,#1e3a6b)}
  .abs{position:absolute}

  /* business cards */
  .card-front{left:74px;top:111px;width:104px;height:59px}
  .card-front .wordmark{left:8px;top:23px;font-size:6px}
  .card-front .divider{left:47px;top:18px;width:.4px;height:22px;background:#b8c3d0}
  .card-front .who{left:52px;top:19px}
  .card-front .who h3{font-family:var(--serif);font-size:3.4px;color:var(--blue);font-weight:700}
  .card-front .who p{font-size:2.4px}
  .card-front .contacts{font-size:2.3px;margin-top:2px}
  .card-front .foot{left:0;right:0;bottom:7px;text-align:center;font-size:2.3px}
  .card-back{left:194px;top:111px;width:104px;height:59px;background:linear-gradient(135deg,var(--blue) 55%,#1a63b4)}
  .card-back h4{font-family:var(--serif);color:#fff;font-size:3.4px;left:8px;top:46px;letter-spacing:.1px}
  .card-back p{color:#dbe8f5;font-size:2.2px;left:8px;top:50.5px}

  /* email signature */
  .email-sig{left:336px;top:108px;width:201px;height:61px;border-bottom:2.4px solid var(--blue)}
  .email-sig .photo{left:10px;top:9px;width:36px;height:36px;border-radius:50%}
  .email-sig .social{left:14px;top:48px;display:flex;gap:2px}
  .email-sig .social i{width:5px;height:5px;border-radius:50%;background:var(--blue);display:block}
  .email-sig .who{left:61px;top:10px}
  .email-sig h3{font-family:var(--serif);font-size:6px;color:var(--blue);font-weight:700}
  .email-sig .role{font-size:4px;margin-bottom:3px}
  .email-sig .contacts{font-size:3.8px}
  .email-sig .addr{left:61px;top:45px;font-size:3.8px}
  .email-sig .wordmark{right:10px;top:10px;font-size:7px}

  /* letterhead */
  .letterhead{left:75px;top:182px;width:223px;height:315px}
  .letterhead .wordmark{left:18px;top:12px;font-size:10px}
  .letterhead .contacts{left:156px;top:15px;border-left:.4px solid #b8c3d0;padding-left:3px}
  .letter{left:23px;top:75px;width:177px;font-size:3.2px;line-height:1.45}
  .letter p{margin-bottom:4px;text-align:justify}
  .letter .sign{width:50px;height:7px;background:linear-gradient(90deg,#cfd6de,#eef1f4);margin-top:2px}
  .letterhead .foot{left:18px;bottom:10px;font-size:3.2px}

  /* proposal cover */
  .proposal{left:313px;top:181px;width:224px;height:315px}
  .proposal .wordmark{left:25px;top:20px;font-size:10px}
  .proposal .contacts{left:148px;top:19px;font-size:3.2px}
  .proposal .title{left:25px;top:130px}
  .proposal .title h2{font-family:var(--serif);font-weight:400;font-size:12.5px;color:var(--ink);line-height:1}
  .proposal .title h1{font-family:var(--serif);font-weight:700;font-size:22px;color:var(--blue);line-height:1.05}
  .proposal .title p{font-size:4px;margin-top:1px}
  .proposal .rule{left:25px;top:180px;width:20px;height:1.6px;background:var(--blue)}
  .proposal .scene{left:0;right:0;top:188px;bottom:0;background:linear-gradient(180deg,#fff 0%,#e4ebf2 30%,#b5c3d2 70%,#7f8fa1 100%)}

  /* slides */
  .slide{width:274px;height:171px;background:var(--slide)}
  .slide-title{left:557px;top:108px}
  .slide-title .scene{inset:0;background:linear-gradient(110deg,var(--slide) 35%,#e3eaf1 65%,#c8d6e4 100%)}
  .slide-title .wordmark{left:20px;top:22px;font-size:8px}
  .slide-title h1{left:20px;top:89px;font-family:var(--serif);font-weight:400;font-size:15px;color:var(--blue)}
  .slide-title .tag{left:20px;top:110px;font-size:7.2px}
  .slide-title .by{left:20px;top:133px;font-size:4.2px;line-height:1.4}
  .slide-title .by b{color:var(--blue)}

  .slide-bio{left:851px;top:108px}
  .slide-bio .band{left:0;top:0;width:90px;height:100%;background:var(--blue)}
  .slide-bio .photo{left:26px;top:22px;width:83px;height:126px}
  .slide-bio .wordmark{right:8px;top:6px;font-size:3.2px}
  .slide-bio .text{left:128px;top:20px;width:132px}
  .slide-bio h2{font-family:var(--serif);font-weight:400;font-size:7.2px;color:var(--blue);line-height:1.15}
  .slide-bio .sub{font-size:4px;color:var(--blue);font-style:italic;margin-top:3px}
  .slide-bio .rule{width:11px;height:1.2px;background:var(--blue);margin:6px 0}
  .slide-bio p{font-size:3.3px;line-height:1.35;text-align:justify;margin-bottom:4px}

  .slide-services{left:557px;top:298px}
  .slide-services .wordmark{right:8px;top:6px;font-size:3.2px}
  .slide-services .rule{left:130px;top:27px;width:13px;height:1.2px;background:var(--blue)}
  .slide-services .lead{left:30px;right:30px;top:34px;text-align:center;font-size:5px;line-height:1.4}
  .svc{top:63px;width:71px;height:88px;background:#fff;border:.5px solid #d5dce4;border-radius:2px;text-align:center;font-size:3.8px;line-height:1.3;padding:52px 5px 0}
  .svc b{font-weight:700}
  .svc svg{position:absolute;left:21px;top:10px;width:29px;height:29px}
  .svc::before{content:"";position:absolute;left:-.5px;top:-.5px;border-top:4px solid var(--blue);border-right:4px solid transparent}
  .svc-1{left:23px}.svc-2{left:101px}.svc-3{left:180px}

  .slide-thanks{left:851px;top:298px}
  .slide-thanks .scene{inset:0;background:linear-gradient(100deg,var(--slide) 50%,#fafbfc 70%,#e4e8ec 100%)}
  .slide-thanks .wordmark{left:22px;top:21px;font-size:6px}
  .slide-thanks h1{left:20px;top:68px;font-family:var(--serif);font-weight:400;font-size:26px;color:var(--blue)}
  .slide-thanks .tag{left:21px;top:99px;font-size:9px}
  .slide-thanks .contacts{left:21px;top:138px;font-size:3.3px}
  .slide-thanks .addr{left:76px;top:141px;font-size:3.3px;line-height:1.5}
  .slide-thanks .acc{left:222px;top:130px;font-size:4px;color:var(--blue);font-weight:700}
  .slide-thanks .badges{left:180px;top:137px;display:flex;gap:5px;align-items:center}
  .slide-thanks .badges i{display:block;background:#c9ced6}
  .slide-thanks .badges i:first-child{width:13px;height:13px;border-radius:50%}
  .slide-thanks .badges i:nth-child(2){width:24px;height:9px}
  .slide-thanks .badges i:last-child{width:22px;height:10px}

  /* compliment slip & envelope */
  .slip{left:111px;top:513px;width:245px;height:107px}
  .slip .wordmark{left:16px;top:15px;font-size:10px}
  .slip .contacts{left:16px;top:80px}
  .slip .addr{left:71px;top:84px;font-size:3.3px;line-height:1.5}
  .envelope{left:372px;top:513px;width:244px;height:107px}
  .envelope svg{position:absolute;left:0;top:0}

  /* project folder (flat, open) */
  .folder-back{left:642px;top:486px;width:220px;height:280px;background:linear-gradient(160deg,#0e5bb0,var(--blue) 50%,#0a3f8a)}
  .folder-back .contacts{left:120px;top:218px;color:#fff;font-size:3.4px}
  .folder-back .contacts li::before{background:#fff}
  .folder-back .wordmark{left:18px;top:244px;font-size:8px;color:#fff}
  .folder-back .wordmark::before{background:#fff}
  .folder-front{left:862px;top:486px;width:220px;height:280px}
  .folder-front svg{position:absolute;inset:0}
  .folder-front .wordmark{left:120px;top:26px;font-size:11px}
  .folder-front .tagline{right:18px;top:244px;text-align:right;color:#fff}
  .folder-front .tagline h4{font-family:var(--serif);font-weight:700;font-size:6.5px;letter-spacing:.3px}
  .folder-front .tagline p{font-size:4.4px}
</style>
</head>
<body>

<!-- Business card: front -->
<section class="piece card-front">
  <div class="abs wordmark"><div><span>Marlow</span><span>Advises</span></div></div>
  <div class="abs divider"></div>
  <div class="abs who">
    <h3>DANIEL MARLOW, PhD</h3>
    <p>Founder</p>
    <ul class="contacts">
      <li>+61 3 9000 1234</li>
      <li>info@marlowadvises.com</li>
      <li>www.marlowadvises.com</li>
    </ul>
  </div>
  <p class="abs foot">Suite 12/40 Elm Row, Fitzroy, Victoria, Australia</p>
</section>

<!-- Business card: back -->
<section class="piece card-back">
  <h4 class="abs">TRANSFORMING CULTURES</h4>
  <p class="abs">One leader, one team, one organisation at a time.</p>
</section>

<!-- Email signature -->
<section class="piece email-sig">
  <div class="abs photo" role="img" aria-label="Round portrait photo of the founder"></div>
  <div class="abs social"><i></i><i></i><i></i><i></i></div>
  <div class="abs who">
    <h3>DANIEL MARLOW, PhD</h3>
    <p class="role">Founder</p>
    <ul class="contacts">
      <li>+61 3 9000 1234</li>
      <li>info@marlowadvises.com</li>
      <li>www.marlowadvises.com</li>
    </ul>
  </div>
  <p class="abs addr">Suite 12/40 Elm Row, Fitzroy, Victoria, Australia</p>
  <div class="abs wordmark"><div><span>Marlow</span><span>Advises</span></div></div>
</section>

<!-- Letterhead -->
<section class="piece letterhead">
  <div class="abs wordmark"><div><span>Marlow</span><span>Advises</span></div></div>
  <ul class="abs contacts">
    <li>+61 3 9000 1234</li>
    <li>info@marlowadvises.com</li>
    <li>www.marlowadvises.com</li>
  </ul>
  <div class="abs letter">
    <p>01 January 2050</p>
    <p>Company (Pvt) Ltd.<br>PO Box 3355 Mainville St<br>Sample City Country 3355</p>
    <p>Dear Paul Harding,</p>
    <p>Thank you for meeting with us last month. As discussed, we propose a staged programme that begins with listening sessions across your senior team, followed by a clear picture of the informal culture that shapes daily decisions, and a shared plan for change that your leaders can own.</p>
    <p>The first phase runs over six weeks and combines interviews, small group workshops and one-to-one coaching. At its close we will present our findings and agree the priorities that matter most to your people and to the performance of the organisation.</p>
    <p>We would welcome the chance to talk through this outline with you and your board. Please let us know a time that suits, and we will prepare a short summary ahead of the conversation.</p>
    <p>Sincerely Yours</p>
    <div class="sign" role="img" aria-label="Handwritten signature of Hugh Adair"></div>
  </div>
  <p class="abs foot">Suite 12/40 Elm Row, Fitzroy, Victoria, Australia</p>
</section>

<!-- Proposal cover -->
<section class="piece proposal">
  <div class="abs wordmark"><div><span>Marlow</span><span>Advises</span></div></div>
  <ul class="abs contacts">
    <li>Suite 12/40 Elm Row</li>
    <li>Fitzroy, Victoria, Australia</li>
    <li>+61 3 9000 1234</li>
    <li>info@marlowadvises.com</li>
    <li>www.marlowadvises.com</li>
  </ul>
  <div class="abs title">
    <h2>BUSINESS PROJECT</h2>
    <h1>PROPOSAL</h1>
    <p>ISSUED DATE: 01 FEB 2022</p>
  </div>
  <div class="abs rule"></div>
  <div class="abs scene" role="img" aria-label="Photo of a water droplet creating ripples on a calm grey-blue surface"></div>
</section>

<!-- Slide: title -->
<section class="piece slide slide-title">
  <div class="abs scene" role="img" aria-label="Soft photo of ripples on pale water"></div>
  <div class="abs wordmark"><div><span>Marlow</span><span>Advises</span></div></div>
  <h1 class="abs">Your Presentation Title</h1>
  <p class="abs tag">Your Best Tagline Goes Here</p>
  <p class="abs by"><b>By Daniel Marlow</b>, PhD<br>Professor<br>Organisational Culture &amp; Leadership</p>
</section>

<!-- Slide: biography -->
<section class="piece slide slide-bio">
  <div class="abs band"></div>
  <div class="abs photo" role="img" aria-label="Portrait photo of the founder in a blue suit outdoors"></div>
  <div class="abs wordmark"><div><span>Marlow</span><span>Advises</span></div></div>
  <div class="abs text">
    <h2>Authentic. Empathic. Purposeful.<br>Trusted.</h2>
    <p class="sub">Daniel Marlow – Professor of Organisational Culture and Leadership</p>
    <div class="rule"></div>
    <p>Daniel is a specialist in the deep cultural change that professionals need in their workplace. Such change operates at the crucial experiential level – that of the informal organisation.</p>
    <p>He helps leading private, public and government organisations catalyse effective cultural change. As a professor at leading universities, he has a specialist focus in executive education and is an accredited coach.</p>
    <p>Before his business-school career, he was a clinical director and lead consultant psychotherapist in major teaching hospitals. He holds a PhD in organisational culture and leadership.</p>
  </div>
</section>

<!-- Slide: services -->
<section class="piece slide slide-services">
  <div class="abs wordmark"><div><span>Marlow</span><span>Advises</span></div></div>
  <div class="abs rule"></div>
  <p class="abs lead">At Marlow Advises, we catalyse the deep cultural change needed<br>to create humane, people-centred workplaces.</p>
  <div class="abs svc svc-1">
    <svg viewBox="0 0 30 30" fill="none" stroke="var(--blue)" stroke-width="1.2"><circle cx="15" cy="15" r="13"/><path d="M9 20 L13 16 L17 18 L21 11"/><path d="M18 11 H21 V14"/></svg>
    <b>Craft sustainable strategies</b> that harness personal motivations, energies and resources.
  </div>
  <div class="abs svc svc-2">
    <svg viewBox="0 0 30 30" fill="none" stroke="var(--blue)" stroke-width="1.2"><circle cx="15" cy="6" r="3"/><circle cx="6" cy="17" r="3"/><circle cx="24" cy="17" r="3"/><circle cx="15" cy="24" r="3"/><circle cx="15" cy="15" r="2"/></svg>
    <b>Build highly effective teams</b> that generate psychological safety and better performance.
  </div>
  <div class="abs svc svc-3">
    <svg viewBox="0 0 30 30" fill="none" stroke="var(--blue)" stroke-width="1.2"><circle cx="15" cy="15" r="13"/><circle cx="15" cy="15" r="10"/><path d="M19 11 L16 16 L11 19 L14 14 Z"/></svg>
    <b>Navigate tricky leadership dynamics</b> to create healthier relationships at work.
  </div>
</section>

<!-- Slide: thank you -->
<section class="piece slide slide-thanks">
  <div class="abs scene" role="img" aria-label="Soft photo of white architectural folds"></div>
  <div class="abs wordmark"><div><span>Marlow</span><span>Advises</span></div></div>
  <h1 class="abs">Thank You</h1>
  <p class="abs tag">Your Best Tagline Goes Here</p>
  <ul class="abs contacts">
    <li>+61 3 9000 1234</li>
    <li>info@marlowadvises.com</li>
    <li>www.marlowadvises.com</li>
  </ul>
  <p class="abs addr">Suite 12/40 Elm Row<br>Fitzroy, Victoria, Australia</p>
  <p class="abs acc">Accredited by</p>
  <div class="abs badges"><i></i><i></i><i></i></div>
</section>

<!-- Compliment slip -->
<section class="piece slip">
  <div class="abs wordmark"><div><span>Marlow</span><span>Advises</span></div></div>
  <ul class="abs contacts">
    <li>+61 3 9000 1234</li>
    <li>info@marlowadvises.com</li>
    <li>www.marlowadvises.com</li>
  </ul>
  <p class="abs addr">Suite 12/40 Elm Row<br>Fitzroy, Victoria, Australia</p>
</section>

<!-- Envelope -->
<section class="piece envelope">
  <svg width="244" height="107" viewBox="0 0 244 107">
    <path d="M0 0 H244 L236 30 Q235 34 230 34 H14 Q9 34 8 30 Z" fill="var(--blue)"/>
    <path d="M2 107 L10 36 M242 107 L234 36" stroke="#e2e5e9" stroke-width=".6"/>
  </svg>
</section>

<!-- Project folder: back cover -->
<section class="piece folder-back">
  <ul class="abs contacts">
    <li>Suite 12/40 Elm Row</li>
    <li>Fitzroy, Victoria, Australia</li>
    <li>+61 3 9000 1234</li>
    <li>info@marlowadvises.com</li>
    <li>www.marlowadvises.com</li>
  </ul>
  <div class="abs wordmark"><div><span>Marlow</span><span>Advises</span></div></div>
</section>

<!-- Project folder: front cover -->
<section class="piece folder-front">
  <svg viewBox="0 0 220 280" preserveAspectRatio="none">
    <defs>
      <linearGradient id="folderBlue" x1="0" y1="0" x2="0" y2="1">
        <stop offset="0" stop-color="#0e5bb0"/>
        <stop offset="1" stop-color="#0a3f8a"/>
      </linearGradient>
    </defs>
    <rect width="220" height="280" fill="#fff"/>
    <path d="M0 60 L220 130 V280 H0 Z" fill="url(#folderBlue)"/>
    <path d="M0 60 L220 130 L220 150 L0 90 Z" fill="#1f2f7a" opacity=".55"/>
  </svg>
  <div class="abs wordmark"><div><span>Marlow</span><span>Advises</span></div></div>
  <div class="abs tagline">
    <h4>TRANSFORMING CULTURES</h4>
    <p>One leader, one team, one organisation at a time.</p>
  </div>
</section>

</body>
</html>
```